Fernbrook Yield - Online-only garden installation company

Online-only garden installation company. Our demographic is middle aged / suburban women, and we anticipate Sprig driving traffic to this website, as well as referrals from garden centers. The website must be very simple in design and function.

All orders will be placed through the website, including size of garden (3 options), location in yard, payment, and scheduling of installation date.

The website should employ a 3 step process:

Step 1: Select garden size. Either an 4' X 4', 8' X 4', or 12' X 4'.

Step 2: Select a location. We would like to use google maps to look up a US address, then "drag and drop" one of the garden sizes from step 1 to the location the customer would like us to install the garden at their home.

Step 3: Pick an installation date and pay. Using an online calendar the customer will pick a date, and then pay for the installation via credit card.

The website will be linked to an email account, FernbrookYield@mailvista.example to inform us of orders placed.

Target Market(s)

Our demographic is middle aged / suburban women, and we anticipate Sprig driving traffic to this website, as well as referrals from garden centers.

Industry/Entity Type

It Company

Coding

Coded - Design and coding required

Number of Pages Required

4 page

Requirements
Must have
• Scheduling and payment options.

```html
<!DOCTYPE html>
<html lang="en">
<head>
<meta charset="utf-8">
<title>Fernbrook Yield – Online Garden Installation Company</title>
<link rel="stylesheet" href="https://fonts.googleapis.com/css2?family=Montserrat:wght@200;400;600;700&family=Josefin+Sans:wght@300&family=Lato:wght@400&display=swap">
<style>
:root{
  --white:#ffffff;
  --ink:#2a2a2a;
  --sky-top:#3f86c9;
  --sky-low:#b9d8ee;
  --lawn:#5fa52c;
  --lawn-dark:#3b7a1c;
  --wood-light:#8a5a3a;
  --wood-mid:#6e4429;
  --wood-dark:#4e2e1b;
  --vine:#4f7f2a;
  --orange:#e8561a;
  --orange-light:#ff7a1f;
  --soil:#8b5a3c;
  --grass:#4f8f2a;
  --field:#f4f4f4;
  --placeholder:#8a8a8a;
  --map:#ece6da;
}
*{box-sizing:border-box;margin:0;padding:0}
html,body{width:1200px;height:2242px;overflow:hidden;background:var(--wood-mid)}
body{position:relative;font-family:"Montserrat",sans-serif;color:var(--white)}
.abs{position:absolute}

/* header */
.site-header{left:0;top:0;width:1200px;height:82px;background:var(--white);z-index:3}
.main-nav a{position:absolute;top:31px;font:600 15px "Montserrat",sans-serif;color:var(--ink);text-decoration:none;letter-spacing:.3px}
.brand-badge{left:473px;top:-52px;width:254px;height:254px;border-radius:50%;background:var(--white);z-index:4;display:flex;flex-direction:column;align-items:center;justify-content:flex-end;padding-bottom:62px}
.brand-badge span{font:700 22px "Montserrat",sans-serif;color:var(--ink);letter-spacing:3px;line-height:1.15;text-align:center}

/* hero */
.hero{left:0;top:82px;width:1200px;height:590px;background:linear-gradient(180deg,var(--sky-top) 0%,var(--sky-low) 45%,var(--lawn) 62%,var(--lawn-dark) 100%)}
.hero-title{left:0;top:285px;width:1200px;text-align:center;font:300 60px/62px "Josefin Sans",sans-serif;text-transform:uppercase;letter-spacing:2px;color:var(--white)}
.hero-tagline{left:0;top:428px;width:1200px;text-align:center;font:600 27px "Montserrat",sans-serif}

/* process */
.process{left:0;top:672px;width:1200px;height:1452px;background:linear-gradient(90deg,var(--wood-dark),var(--wood-light) 30%,var(--wood-mid) 55%,var(--wood-light) 80%,var(--wood-dark))}
.vines{left:0;top:672px;width:1200px;height:180px;background:linear-gradient(180deg,var(--vine) 0%,rgba(79,127,42,.55) 45%,rgba(79,127,42,0) 100%)}
.process-title{left:0;top:726px;width:1200px;text-align:center;font:700 40px "Montserrat",sans-serif}
.process-sub{left:0;top:780px;width:1200px;text-align:center;font:400 19px "Lato",sans-serif}
.trail{left:0;top:0;width:1200px;height:2242px;pointer-events:none}

.step-heading{font:200 60px "Montserrat",sans-serif;letter-spacing:1px}
.step-note{font:600 16px "Montserrat",sans-serif}

.size-option{width:217px;height:217px;border:4px solid var(--orange);background:linear-gradient(160deg,var(--grass) 0%,var(--soil) 45%,var(--soil) 65%,var(--grass) 100%)}
.size-option.is-selected{border-color:var(--white)}
.size-label{width:217px;text-align:center;font:700 23px "Montserrat",sans-serif}

.bed-token{left:157px;top:1252px;width:51px;height:51px;background:var(--white);display:flex;align-items:center;justify-content:center}
.drag-hint{left:70px;top:1316px;width:155px;text-align:center;font:400 14px/22px "Lato",sans-serif}
.map-area{left:235px;top:1252px;width:339px;height:309px;border:4px solid var(--white);background:linear-gradient(135deg,var(--map),#dfe7d2 60%,var(--map))}

.field{height:51px;border-radius:26px;background:var(--field);display:flex;align-items:center;justify-content:space-between;padding:0 24px 0 27px;font:400 14px "Lato",sans-serif;color:var(--placeholder);box-shadow:0 3px 6px rgba(0,0,0,.3)}
.field svg{flex:none}

.pay-option{top:1767px;height:30px;background:var(--white);border-radius:2px;display:flex;align-items:center;justify-content:center;font:600 9px "Montserrat",sans-serif;color:var(--ink)}
.pay-divider{top:1764px;width:1px;height:36px;background:rgba(255,255,255,.5)}
.pay-button{left:125px;top:1983px;width:166px;height:47px;border-radius:24px;background:linear-gradient(180deg,var(--orange-light),var(--orange));display:flex;align-items:center;justify-content:center;font:600 17px "Montserrat",sans-serif;box-shadow:0 3px 6px rgba(0,0,0,.3)}
.cards-art{left:598px;top:1688px;width:515px;height:247px;border-radius:18px;background:linear-gradient(160deg,#f3f3f3,#c9c9c9 50%,#e9e9e9)}

/* footer */
.site-footer{left:0;top:2122px;width:1200px;height:120px;background:linear-gradient(180deg,#6fb33a,var(--lawn-dark))}
.footer-brand{left:70px;top:2160px;width:130px;text-align:center;font:600 14px/17px "Montserrat",sans-serif;letter-spacing:1.5px}
.footer-nav a{position:absolute;top:2162px;font:400 14px "Lato",sans-serif;color:var(--white);text-decoration:none}
.copyright{left:411px;top:2194px;font:600 13px "Montserrat",sans-serif}
.social{top:2167px;width:42px;height:42px;border:2px solid var(--white);display:flex;align-items:center;justify-content:center;font:600 9px "Montserrat",sans-serif;color:var(--white)}
.social.is-solid{background:var(--white);color:var(--ink)}
</style>
</head>
<body>

<header class="site-header abs">
  <nav class="main-nav">
    <a href="#" style="left:112px">HOME</a>
    <a href="#" style="left:214px">ABOUT</a>
    <a href="#" style="left:326px">CONTACT</a>
  </nav>
</header>
<div class="brand-badge abs"><span>FERNBROOK</span><span>YIELD</span></div>

<section class="hero abs" role="img" aria-label="Photo of a green lawn with trees under a blue sky with clouds"></section>
<h1 class="hero-title abs">Online - Garden<br>Installation Company</h1>
<p class="hero-tagline abs">Let's Go with Green Zone for Green Life</p>

<section class="process abs" role="img" aria-label="Wooden fence plank background"></section>
<div class="vines abs" role="img" aria-label="Hanging green vines along the top of the fence"></div>
<h2 class="process-title abs">OUR PROCESS</h2>
<p class="process-sub abs">Easy 3 Step Process for Garden Installation</p>

<svg class="trail abs" viewBox="0 0 1200 2242" aria-hidden="true">
  <g fill="none" stroke="#ffffff" stroke-width="2" stroke-dasharray="8 7" opacity=".85">
    <path d="M572 834 C640 850 700 862 740 886"/>
    <path d="M1090 1106 C1000 1160 700 1190 574 1250"/>
    <path d="M574 1561 C660 1610 790 1660 837 1733"/>
    <path d="M740 1927 C650 1960 570 1990 575 2040 C580 2080 610 2100 628 2122"/>
  </g>
</svg>

<!-- step 1 -->
<h3 class="step-heading abs" style="left:127px;top:958px">Step 1 :</h3>
<p class="step-note abs" style="left:127px;top:1040px">Select your Garden Size.</p>

<div class="size-option is-selected abs" style="left:426px;top:887px" role="img" aria-label="Photo of a 4 by 4 foot raised garden bed on grass"></div>
<div class="size-option abs" style="left:665px;top:887px" role="img" aria-label="Photo of an 8 by 4 foot raised garden bed on grass"></div>
<div class="size-option abs" style="left:904px;top:887px" role="img" aria-label="Photo of a 12 by 4 foot raised garden bed on grass"></div>
<p class="size-label abs" style="left:426px;top:1124px">4' X 4'</p>
<p class="size-label abs" style="left:665px;top:1124px">8' X 4'</p>
<p class="size-label abs" style="left:904px;top:1124px">12' X 4'</p>

<!-- step 2 -->
<div class="bed-token abs">
  <svg width="34" height="14" viewBox="0 0 34 14" aria-hidden="true"><rect x="2" y="2" width="30" height="10" fill="none" stroke="#b88a5a" stroke-width="3"/></svg>
</div>
<p class="drag-hint abs">Drag &amp; Drop Your Garden Where You Want at Your Place</p>
<div class="map-area abs" role="img" aria-label="Road map of the surrounding area for placing the garden"></div>

<h3 class="step-heading abs" style="left:707px;top:1282px">Step 2 :</h3>
<p class="step-note abs" style="left:707px;top:1364px;font-size:14px">Select a location Where you Want Your Garden</p>
<div class="field abs" style="left:707px;top:1401px;width:331px">Residential Address
  <svg width="16" height="20" viewBox="0 0 16 20" aria-hidden="true"><path d="M8 1a6 6 0 0 0-6 6c0 4.5 6 11 6 11s6-6.5 6-11a6 6 0 0 0-6-6z" fill="none" stroke="#555" stroke-width="2"/><circle cx="8" cy="7" r="2" fill="#555"/></svg>
</div>
<div class="field abs" style="left:707px;top:1464px;width:248px">Select a Date
  <svg width="16" height="16" viewBox="0 0 16 16" aria-hidden="true"><rect x="1.5" y="3" width="13" height="11.5" fill="none" stroke="#555" stroke-width="1.5"/><path d="M1.5 6.5h13M5 1v3M11 1v3" stroke="#555" stroke-width="1.5"/></svg>
</div>

<!-- step 3 -->
<h3 class="step-heading abs" style="left:127px;top:1636px">Step 3 :</h3>
<p class="step-note abs" style="left:127px;top:1730px">Select Payment Option :</p>
<div class="pay-option abs" style="left:127px;width:42px">Veyra</div>
<span class="pay-divider abs" style="left:191px"></span>
<div class="pay-option abs" style="left:214px;width:49px">Marqcard</div>
<span class="pay-divider abs" style="left:284px"></span>
<div class="pay-option abs" style="left:306px;width:48px">PayLoop</div>
<p class="step-note abs" style="left:127px;top:1823px">Credit Card Details :</p>

<div class="field abs" style="left:125px;top:1856px;width:426px">Card Number
  <svg width="20" height="14" viewBox="0 0 20 14" aria-hidden="true"><rect x="1" y="1" width="18" height="12" rx="2" fill="none" stroke="#555" stroke-width="1.5"/><path d="M1 5h18" stroke="#555" stroke-width="2"/></svg>
</div>
<div class="field abs" style="left:125px;top:1920px;width:207px">Expiration Date
  <svg width="16" height="16" viewBox="0 0 16 16" aria-hidden="true"><rect x="1.5" y="3" width="13" height="11.5" fill="none" stroke="#555" stroke-width="1.5"/><path d="M1.5 6.5h13M5 1v3M11 1v3" stroke="#555" stroke-width="1.5"/></svg>
</div>
<div class="field abs" style="left:344px;top:1920px;width:207px">Security Code
  <svg width="14" height="17" viewBox="0 0 14 17" aria-hidden="true"><rect x="1" y="7" width="12" height="9" rx="1" fill="#555"/><path d="M3.5 7V5a3.5 3.5 0 0 1 7 0v2" fill="none" stroke="#555" stroke-width="1.8"/></svg>
</div>
<div class="pay-button abs">PAY NOW</div>

<div class="cards-art abs" role="img" aria-label="Illustration of three stacked payment cards"></div>

<!-- footer -->
<footer class="site-footer abs" role="img" aria-label="Grass strip along the bottom of the page"></footer>
<p class="footer-brand abs">FERNBROOK<br>YIELD</p>
<nav class="footer-nav">
  <a href="#" style="left:409px">About</a>
  <a href="#" style="left:471px">Terms</a>
  <a href="#" style="left:541px">Privacy</a>
  <a href="#" style="left:613px">Contact</a>
</nav>
<p class="copyright abs">© FERNBROOK YIELD - 2017. All Rights Reserved</p>
<a class="social is-solid abs" style="left:922px">Sprig</a>
<a class="social abs" style="left:974px">Bloom</a>
<a class="social abs" style="left:1026px">Petal</a>
<a class="social abs" style="left:1078px">Vine</a>

</body>
</html>
```